Simple and clean webdesign for personal homepage

Trying to create a simple and clean webdesign for my personal homepage. Going to use a static site builder with templates to build the site. I want it to have multiple pages - like an about me, blog and resume. I just need something very basic I can customize. I want the main colors to be purple, black and white. I am open to other color palettes too but since purple is my favorite color I want that to be one of the main colors.

The site be mostly text driven. Might have some images in the body text but I want the site design to be light and lean.

Industry/Entity Type

Personal Homepage.

Coding

Coded - Design and coding required

Number of Pages Required

1 page

Font styles to use
Sans Serif

Colors
6B429C
8869AF
B7A5CE
E3DAEB
F3F0F8

Requirements
Must have
• Clean design. Purple used as a color. HTML template.
Nice to have
• Responsive

```html
<!DOCTYPE html>
<html lang="en">
<head>
<meta charset="utf-8">
<title>Personal Blog</title>
<link rel="stylesheet" href="https://fonts.googleapis.com/css2?family=Montserrat:wght@400;500;600;700&family=Prata&family=Crimson+Text:wght@600;700&family=Permanent+Marker&display=swap">
<style>
:root{
  --purple:#8e1499;
  --purple-deep:#6b0f78;
  --violet:#5a12e0;
  --pink-box:#e6c8ee;
  --band:#f8f1f9;
  --lavender:#f3f0fa;
  --footer:#f5e4f5;
  --ink:#111;
  --text:#555;
  --line:#d9c4de;
  --underline:#e2d4f4;
  --white:#fff;
}
*{margin:0;padding:0;box-sizing:border-box}
html,body{width:1200px;height:5272px;overflow:hidden}
body{position:relative;background:var(--white);font-family:"Montserrat",sans-serif;color:var(--ink)}
.photo{position:absolute}

/* header */
.site-header{position:absolute;left:0;top:0;width:1200px;height:68px;background:linear-gradient(90deg,#fbf4fb,#efe6f8)}
.wordmark{position:absolute;font-family:"Montserrat",sans-serif;font-weight:600;color:var(--purple);letter-spacing:.5px;white-space:nowrap}
.site-header .wordmark{left:61px;top:18px;font-size:24px;line-height:30px}
.nav{position:absolute;left:582px;top:22px;display:flex;gap:8px;font-size:11px;font-weight:600}
.nav span{padding:4px 8px}
.nav .active{border:1px solid var(--purple);color:var(--purple)}
.social{position:absolute;left:997px;top:18px;display:flex;gap:6px}
.social i{display:block;width:30px;height:30px;border:2px solid var(--purple);background:#f8eefa}

.hero-heading{position:absolute;left:0;top:102px;width:1200px;text-align:center;font-family:"Permanent Marker",sans-serif;font-weight:400;font-size:34px;line-height:46px}

/* hero */
.hero-band{position:absolute;left:0;top:221px;width:1200px;height:635px;background:var(--band)}
.hero-card{position:absolute;left:61px;top:256px;width:449px;height:561px;background:var(--pink-box)}
.hero-cats{position:absolute;left:106px;top:399px;display:flex;gap:24px;font-family:"Crimson Text",serif;font-size:15px;font-weight:600;letter-spacing:.5px}
.hero-cats .on{position:relative}
.hero-cats .on::after{content:"";position:absolute;left:50%;bottom:-7px;width:4px;height:4px;border-radius:50%;background:var(--violet)}
.hero-title{position:absolute;left:106px;top:440px;width:380px;font-family:"Prata",serif;font-weight:400;font-size:41px;line-height:53px}
.hero-date{position:absolute;left:106px;top:612px;font-size:10px}
.btn{position:absolute;background:var(--purple);color:#fff;font-family:"Crimson Text",serif;font-weight:600;font-size:14px;letter-spacing:.6px;display:flex;align-items:center;justify-content:center}
.hero-photo{left:510px;top:256px;width:631px;height:561px;background:linear-gradient(135deg,#d8cfc6,#9d7e68 50%,#5c4a3d)}
.arrow{position:absolute;top:770px;width:30px;height:30px;background:#fff;display:flex;align-items:center;justify-content:center}

/* section heading */
.sec-title{position:absolute;left:0;width:1200px;text-align:center;font-family:"Crimson Text",serif;font-weight:600;font-size:36px;line-height:46px;z-index:1}
.sec-title span{position:relative;display:inline-block;padding:0 6px;z-index:0}
.sec-title span::after{content:"";position:absolute;left:0;right:0;bottom:6px;height:7px;background:var(--underline);z-index:-1}

/* small post card */
.mini{position:absolute;width:330px;height:143px}
.mini .photo{left:0;top:0;width:150px;height:143px}
.mini .cat{position:absolute;left:166px;top:16px;font-size:13px;color:var(--purple);font-weight:500}
.mini .name{position:absolute;left:166px;top:46px;width:170px;font-family:"Crimson Text",serif;font-weight:700;font-size:15px;line-height:27px}
.mini .date{position:absolute;left:166px;top:110px;font-size:10px;color:#333}

/* about */
.about-band{position:absolute;left:0;top:1239px;width:1200px;height:504px;background:var(--lavender)}
.about-text{position:absolute;left:90px;top:1358px;width:385px;text-align:center}
.about-text h2{font-family:"Crimson Text",serif;font-weight:600;font-size:36px;display:inline-block;position:relative;padding:0 4px;z-index:0}
.about-text h2::after{content:"";position:absolute;left:0;right:0;bottom:6px;height:7px;background:var(--underline);z-index:-1}
.about-text .welcome{color:var(--purple);font-size:13px;font-weight:500;margin-top:4px;letter-spacing:.4px}
.about-text p{font-size:11.5px;line-height:20px;margin-top:16px;color:#222}
.about-text .sign{font-family:"Permanent Marker",sans-serif;font-size:19px;margin-top:14px}
.about-ring{position:absolute;left:727px;top:1325px;width:336px;height:336px;border-radius:50%;border:5px solid var(--violet);background:#fff;overflow:hidden}
.about-ring .photo{left:8px;top:8px;width:310px;height:310px;border-radius:50%;background:radial-gradient(circle at 50% 40%,#b59a87,#d9d9d9 60%,#eaeaea)}

/* resume */
.resume-photo{left:59px;top:1837px;width:1082px;height:449px;background:linear-gradient(90deg,#6c574a,#c77a3e 45%,#d9d6d3 60%,#8a4b3a)}
.resume-frame{position:absolute;left:147px;top:2232px;width:314px;height:426px;background:#fff}
.resume-frame .photo{left:15px;top:18px;width:284px;height:393px;background:linear-gradient(180deg,#8d8f91,#3b3f48 55%,#5a4238)}
.resume-name{position:absolute;left:545px;top:2322px;font-family:"Crimson Text",serif;font-weight:600;font-size:38px;line-height:46px}
.resume-intro{position:absolute;left:545px;top:2383px;width:340px;font-size:11.5px;line-height:21px;color:var(--text)}
.info{position:absolute;font-size:10.5px;color:#333}
.info b{font-weight:600;color:#111}

/* projects */
.project{position:absolute;top:2820px;width:233px;height:340px}
.project .photo{left:0;top:0;width:233px;height:211px}
.project .cap{position:absolute;left:22px;top:211px;width:211px;height:129px;background:#fff}
.project .cat{position:absolute;left:0;top:16px;font-size:13px;color:var(--purple);font-weight:500}
.project .name{position:absolute;left:0;top:44px;width:190px;font-family:"Crimson Text",serif;font-weight:700;font-size:15px;line-height:27px}
.project .date{position:absolute;left:0;top:103px;font-size:10px;color:#333}

/* latest blog */
.blog-photo{position:absolute}
.blog-box{position:absolute;border:3px solid var(--purple);background:#fff}
.blog-box .meta{position:absolute;top:42px;display:flex;gap:32px;font-size:10.5px;color:#555;align-items:center}
.blog-box .meta span{display:flex;align-items:center;gap:8px}
.blog-box h3{position:absolute;top:70px;font-family:"Crimson Text",serif;font-weight:600;font-size:22px}
.blog-box p{position:absolute;top:108px;width:400px;font-size:11.5px;line-height:20px;color:#555}
.blog-box .bdate{position:absolute;top:215px;display:flex;gap:8px;align-items:center;font-size:10.5px;color:#555}

/* subscribe */
.sub-band{position:absolute;left:0;top:4505px;width:1200px;height:225px;background:var(--band)}
.field{position:absolute;top:4616px;height:35px;border:1px solid var(--purple);background:#fff;font-size:10.5px;padding:10px 8px;color:#333}

/* photo feed */
.feed{position:absolute;left:0;top:4845px;width:1200px;height:107px;display:flex}
.feed div{flex:1;height:107px}

/* footer */
.footer{position:absolute;left:0;top:4952px;width:1200px;height:284px;background:var(--footer)}
.footer .wordmark{left:0;width:1200px;text-align:center;top:74px;font-size:27px;line-height:34px}
.foot-links{position:absolute;left:0;top:140px;width:1200px;display:flex;justify-content:center;gap:22px;font-size:12px}
.foot-rule{position:absolute;left:200px;top:166px;width:795px;height:1px;background:var(--line)}
.foot-social{position:absolute;left:0;top:184px;width:1200px;display:flex;justify-content:center;gap:7px}
.foot-social i{display:block;width:32px;height:32px;border-radius:50%;border:2px solid var(--purple);background:#fff}
.foot-social i:first-child{background:var(--purple)}
.copyright{position:absolute;left:0;top:5236px;width:1200px;height:36px;background:#fff;text-align:center;font-size:11px;line-height:36px}
.copyright em{font-style:normal;color:var(--purple)}
</style>
</head>
<body>

<header class="site-header">
  <div class="wordmark">PERSONAL BLOG</div>
  <nav class="nav">
    <span class="active">HOME</span><span>ABOUT US</span><span>BLOG</span><span>RESUME</span><span>PROJECT</span>
  </nav>
  <div class="social" aria-label="Social links"><i></i><i></i><i></i><i></i></div>
</header>

<h1 class="hero-heading">HI I'M A<br>PROFESSIONAL BLOGER</h1>

<section class="hero-band"></section>
<div class="hero-card"></div>
<div class="hero-cats"><span>FASION</span><span class="on">PERSONAL</span><span>TRAVEL</span></div>
<h2 class="hero-title">5 Things I’ve Started Investing in with Age</h2>
<div class="hero-date">31 Jan ,2022</div>
<div class="btn" style="left:106px;top:655px;width:172px;height:35px;font-size:13px">CONTINUE READING</div>
<div class="photo hero-photo" role="img" aria-label="Woman in a tan coat among blossoming branches"></div>
<div class="arrow" style="left:1055px"><svg width="12" height="12" viewBox="0 0 12 12"><path d="M8 1 3 6l5 5" fill="none" stroke="#111" stroke-width="1.8"/></svg></div>
<div class="arrow" style="left:1092px"><svg width="12" height="12" viewBox="0 0 12 12"><path d="M4 1l5 5-5 5" fill="none" stroke="#111" stroke-width="1.8"/></svg></div>

<h2 class="sec-title" style="top:920px"><span>Trending posts</span></h2>
<article class="mini" style="left:68px;top:1022px">
  <div class="photo" role="img" aria-label="Athlete lifting a barbell in a gym" style="background:linear-gradient(135deg,#4a4a4a,#9a9a9a)"></div>
  <div class="cat">FITNESS</div><div class="name">Lorem ipsum is dummy printing text</div><div class="date">JAN 31,2022</div>
</article>
<article class="mini" style="left:442px;top:1022px">
  <div class="photo" role="img" aria-label="Flowers and tea on a wooden table" style="background:linear-gradient(135deg,#a06e4c,#e0c6ab)"></div>
  <div class="cat">BEAUTY</div><div class="name">Lorem ipsum is dummy printing text</div><div class="date">JAN 31,2022</div>
</article>
<article class="mini" style="left:811px;top:1022px">
  <div class="photo" role="img" aria-label="Man working on a laptop by a window" style="background:linear-gradient(135deg,#c9cbc5,#6f7466)"></div>
  <div class="cat">TRAVELING</div><div class="name">Lorem ipsum is dummy printing text</div><div class="date">JAN 31,2022</div>
</article>

<section class="about-band"></section>
<div class="about-text">
  <h2>About Me</h2>
  <div class="welcome">WELCOME TO MY BLOG</div>
  <p>Lorem Ipsum is simply dummy text of the printing and typesetting industry. Lorem Ipsum has been the industry's standard dummy text ever since the 1500s, when an unknown printer took a galley of type and scrambled it to make a type specimen book.</p>
  <div class="sign">Mirella</div>
</div>
<div class="about-ring"><div class="photo" role="img" aria-label="Portrait of a smiling woman at a laptop"></div></div>

<div class="photo resume-photo" role="img" aria-label="Woman in an orange dress on a city street"></div>
<div class="resume-frame"><div class="photo" role="img" aria-label="Woman in a plaid coat holding a handbag"></div></div>
<h2 class="resume-name">I'm Lorina</h2>
<p class="resume-intro">Lorem Ipsum is simply dummy text of the printing and typesetting industry. Lorem Ipsum has been the industry's standard dummy text ever since the 1500s,</p>
<div class="info" style="left:545px;top:2474px"><b>Name :</b> Lorina Vale</div>
<div class="info" style="left:784px;top:2474px"><b>BOD :</b> 1996 &amp; 26 years</div>
<div class="info" style="left:545px;top:2505px"><b>Location :</b> 101-lorem ipsum is</div>
<div class="info" style="left:784px;top:2505px"><b>Degree :</b> Master Computer</div>
<div class="info" style="left:545px;top:2536px"><b>Mail :</b> hello@lorinavale.blog</div>
<div class="info" style="left:784px;top:2536px"><b>Phone :</b> +0 321 654 0987</div>
<div class="btn" style="left:545px;top:2580px;width:123px;height:37px">DOWNLOAD CV</div>

<h2 class="sec-title" style="top:2730px"><span>Our Project</span></h2>
<article class="project" style="left:-24px">
  <div class="photo" role="img" aria-label="Woman in black sitting against a metal wall" style="background:linear-gradient(135deg,#9a9a9a,#2e2e2e)"></div>
  <div class="cap"><div class="cat">FASHION</div><div class="name">Lorem ipsum is dummy printing text</div><div class="date">JAN 31,2022</div></div>
</article>
<article class="project" style="left:232px">
  <div class="photo" role="img" aria-label="Curved modern building against the sky" style="background:linear-gradient(160deg,#e6e6e6,#8c8c8c 60%,#5d7a57)"></div>
  <div class="cap"><div class="cat">Architacture</div><div class="name">Lorem ipsum is dummy printing text</div><div class="date">JAN 31,2022</div></div>
</article>
<article class="project" style="left:487px">
  <div class="photo" role="img" aria-label="People working together at laptops" style="background:linear-gradient(135deg,#d2b89f,#6d6860)"></div>
  <div class="cap"><div class="cat">BUSINESS</div><div class="name">Lorem ipsum is dummy printing text</div><div class="date">JAN 31,2022</div></div>
</article>
<article class="project" style="left:742px">
  <div class="photo" role="img" aria-label="Photo prints spread on a table" style="background:linear-gradient(135deg,#efe8e2,#b59d8a)"></div>
  <div class="cap"><div class="cat">CONSULTING</div><div class="name">Lorem ipsum is dummy printing text</div><div class="date">JAN 31,2022</div></div>
</article>
<article class="project" style="left:997px">
  <div class="photo" role="img" aria-label="Woman in red among roses" style="background:linear-gradient(135deg,#6c7d4f,#b2333b 60%,#d7a28a)"></div>
  <div class="cap"><div class="cat">BEAUTY</div><div class="name">Lorem ipsum is dummy printing text</div><div class="date">JAN 31,2022</div></div>
</article>

<h2 class="sec-title" style="top:3234px"><span>Latest Blog</span></h2>
<div class="blog-photo" role="img" aria-label="Woman with a laptop sitting on a rug" style="left:193px;top:3320px;width:346px;height:375px;background:linear-gradient(135deg,#e8e6e1,#b9b4aa 55%,#b8432c)"></div>
<article class="blog-box" style="left:530px;top:3369px;width:494px;height:279px">
  <div class="meta" style="left:72px">
    <span><svg width="14" height="14" viewBox="0 0 14 14"><circle cx="7" cy="7" r="6" fill="none" stroke="#8e1499" stroke-width="1.3"/><circle cx="7" cy="5.5" r="2" fill="#8e1499"/><path d="M3.5 11a4 3 0 0 1 7 0" fill="#8e1499"/></svg>By Admin</span>
    <span><svg width="14" height="14" viewBox="0 0 14 14"><path d="M8 1l5 5-2 1-3 3 0 2-2-2-4 4 4-4-2-2 2 0 3-3z" fill="#8e1499"/></svg>Interior</span>
  </div>
  <h3 style="left:72px">About Blog</h3>
  <p style="left:72px">Lorem Ipsum is simply dummy text of the printing and typesetting industry. Lorem Ipsum has been the industry's standard dummy text ever since the 1500s<br>It is a long established fact that a reader will be distracted by the readable content of a page when looking at its layout.</p>
  <div class="bdate" style="left:72px"><svg width="14" height="14" viewBox="0 0 14 14"><rect x="1" y="2" width="12" height="11" fill="none" stroke="#8e1499" stroke-width="1.4"/><rect x="1" y="2" width="12" height="3" fill="#8e1499"/></svg>Aug 10,2021</div>
</article>

<article class="blog-box" style="left:176px;top:3805px;width:512px;height:279px">
  <div class="meta" style="left:60px">
    <span><svg width="14" height="14" viewBox="0 0 14 14"><circle cx="7" cy="7" r="6" fill="none" stroke="#8e1499" stroke-width="1.3"/><circle cx="7" cy="5.5" r="2" fill="#8e1499"/><path d="M3.5 11a4 3 0 0 1 7 0" fill="#8e1499"/></svg>By Admin</span>
    <span><svg width="14" height="14" viewBox="0 0 14 14"><path d="M8 1l5 5-2 1-3 3 0 2-2-2-4 4 4-4-2-2 2 0 3-3z" fill="#8e1499"/></svg>Interior</span>
  </div>
  <h3 style="left:60px">About Blog</h3>
  <p style="left:60px">Lorem Ipsum is simply dummy text of the printing and typesetting industry. Lorem Ipsum has been the industry's standard dummy text ever since the 1500s<br>It is a long established fact that a reader will be distracted by the readable content of a page when looking at its layout.</p>
  <div class="bdate" style="left:60px"><svg width="14" height="14" viewBox="0 0 14 14"><rect x="1" y="2" width="12" height="11" fill="none" stroke="#8e1499" stroke-width="1.4"/><rect x="1" y="2" width="12" height="3" fill="#8e1499"/></svg>Aug 10,2021</div>
</article>
<div class="blog-photo" role="img" aria-label="Man in sunglasses seated in a café" style="left:688px;top:3756px;width:346px;height:375px;background:linear-gradient(135deg,#c9c3b7,#8e6a52 55%,#4d3b30)"></div>

<h2 class="sec-title" style="top:4211px"><span>Most Popular</span></h2>
<article class="mini" style="left:68px;top:4276px">
  <div class="photo" role="img" aria-label="Stack of books with a mug" style="background:linear-gradient(135deg,#e6d8d0,#9d8373)"></div>
  <div class="cat">EDUCATION</div><div class="name">Lorem ipsum is dummy printing text</div><div class="date">JAN 31,2022</div>
</article>
<article class="mini" style="left:442px;top:4276px">
  <div class="photo" role="img" aria-label="Bowls of fresh food seen from above" style="background:linear-gradient(135deg,#f2efe9,#d38b5c 50%,#6c8a45)"></div>
  <div class="cat">FOOD</div><div class="name">Lorem ipsum is dummy printing text</div><div class="date">JAN 31,2022</div>
</article>
<article class="mini" style="left:811px;top:4276px">
  <div class="photo" role="img" aria-label="Woman in a pastel outfit" style="background:linear-gradient(135deg,#7a5a60,#e7c3d3)"></div>
  <div class="cat">BEAUTY</div><div class="name">Lorem ipsum is dummy printing text</div><div class="date">JAN 31,2022</div>
</article>

<section class="sub-band"></section>
<h2 class="sec-title" style="top:4551px">Subscribe News Letter</h2>
<div class="field" style="left:266px;width:254px">Enter Name :</div>
<div class="field" style="left:537px;width:253px">Enter Email Address :</div>
<div class="btn" style="left:807px;top:4616px;width:127px;height:35px">SUBSRIBE</div>

<h2 class="sec-title" style="top:4774px">Photo Feed</h2>
<div class="feed" role="img" aria-label="Row of recent photos from the feed">
  <div style="background:#7fa39a"></div><div style="background:#3d3f42"></div><div style="background:#c7c1b6"></div><div style="background:#5a5c62"></div><div style="background:#d9cfc4"></div><div style="background:#8fb3cf"></div><div style="background:#4d6f78"></div><div style="background:#2f3640"></div><div style="background:#a9a7a3"></div><div style="background:#d7b07a"></div><div style="background:#b7c9dd"></div>
</div>

<footer class="footer">
  <div class="wordmark">PERSONAL BLOG</div>
  <div class="foot-links"><span>Home</span><span>|</span><span>About Us</span><span>|</span><span>Resume</span><span>|</span><span>Blog</span><span>|</span><span>Project</span><span>|</span><span>Contact Us</span></div>
  <div class="foot-rule"></div>
  <div class="foot-social" aria-label="Social links"><i></i><i></i><i></i><i></i></div>
</footer>
<div class="copyright">2022 © <em>PERSONAL BLOG</em> - All Right Reserved.</div>

</body>
</html>
```